web site update

I want to get a better website for a small high end remodeling and construction company
I currently have a web site but you will find that it is not good.
www.quenbrickhall.com
We are a high end construction / remodeling company that has been in business since 2003. We primarily work in the mid peninsula of the bay area. Most of our clientele are very educated captains of industry. This group is still the target client.
I had my logo designed by Mint Easel a few years ago and I do like it, I like the orange and black or orange a blue. I don’t have a lot of content on hand as far as professional photographs.
Number of pages not sure and are open to: design pages vs full function website
I think what I am after is a web presence that will seal the deal as we are getting high referrals from past clients.
Construction
1 page

```html
<!DOCTYPE html>
<html lang="en">
<head>
<meta charset="utf-8">
<title>Quenbrick Hall — Your Premier Partner</title>
<link rel="stylesheet" href="https://fonts.googleapis.com/css2?family=Lato:ital,wght@0,400;1,700;1,900&family=Montserrat:wght@400;600;700&display=swap">
<style>
  :root {
    --orange: #ff6a00;
    --black: #111111;
    --nav-black: #0b0b0b;
    --footer: #1c1c1c;
    --white: #ffffff;
    --muted: #e6e6e6;
    --night-1: #1b2b57;
    --night-2: #2c4580;
    --night-3: #3a4a6e;
  }
  * { box-sizing: border-box; margin: 0; padding: 0; }
  html, body { width: 1200px; height: 1200px; overflow: hidden; background: var(--footer); }
  .page { position: relative; width: 1200px; height: 1200px; font-family: "Montserrat", sans-serif; color: var(--white); }

  .hero {
    position: absolute; left: 0; top: 0; width: 1200px; height: 845px;
    background:
      radial-gradient(ellipse at 20% 30%, rgba(140,120,110,.55), transparent 45%),
      radial-gradient(ellipse at 50% 95%, rgba(230,170,90,.35), transparent 40%),
      linear-gradient(180deg, var(--night-3) 0%, var(--night-2) 45%, var(--night-1) 100%);
  }

  .main-nav {
    position: absolute; left: 82px; top: 60px; width: 1002px; height: 40px;
    background: var(--nav-black); display: flex; align-items: center;
    font-weight: 700; font-size: 15px; letter-spacing: .2px;
  }
  .main-nav a { position: absolute; color: var(--white); text-decoration: none; }
  .client-login { display: flex; align-items: center; gap: 8px; font-weight: 400; font-size: 14px; }

  .brand {
    position: absolute; left: 480px; top: 5px; width: 240px; height: 134px;
    background: var(--orange); display: flex; align-items: center; justify-content: center;
  }
  .brand-plate {
    width: 200px; height: 80px; background: var(--white);
    display: flex; align-items: center; justify-content: center; gap: 10px;
  }
  .brand-square { width: 34px; height: 34px; background: var(--black); }
  .brand-name { font-family: "Montserrat", sans-serif; font-weight: 700; font-size: 17px; line-height: 1.1; color: var(--black); letter-spacing: .5px; }

  .tagline {
    position: absolute; left: 0; top: 245px; width: 1174px; text-align: center;
    font-family: "Lato", sans-serif; font-style: italic; font-weight: 900; font-size: 62px;
    text-shadow: 0 2px 6px rgba(0,0,0,.35);
  }
  .tagline-sub {
    position: absolute; left: 0; top: 320px; width: 1174px; text-align: center;
    font-family: "Lato", sans-serif; font-size: 27px; line-height: 36px;
  }

  .services {
    position: absolute; left: 85px; top: 453px; width: 1007px; display: grid;
    grid-template-columns: repeat(4, 1fr); column-gap: 2px;
  }
  .service-tab {
    height: 47px; background: #1e1e1e; display: flex; align-items: center; justify-content: center;
    font-weight: 600; font-size: 18px; text-transform: uppercase;
  }
  .service-tab.is-active { background: var(--orange); }
  .service-photo { height: 234px; }
  .photo-development { background: linear-gradient(160deg, #25335a, #3f5f86 50%, #b58a4a); }
  .photo-realestate { background: linear-gradient(170deg, #3a5a86, #c47a2a 55%, #3a3a2a); }
  .photo-property { background: linear-gradient(150deg, #e8c9a0, #c7306a 60%, #5a1a2a); }
  .photo-construction { background: linear-gradient(180deg, #8fa4b8, #6b6f70 55%, #44484a); }

  .slider-arrow { position: absolute; top: 530px; }

  .footer-col { position: absolute; top: 910px; }
  .footer-title { font-weight: 600; font-size: 17px; text-transform: uppercase; margin-bottom: 16px; }
  .footer-list { list-style: none; font-size: 14px; line-height: 21px; color: var(--muted); }
  .newsletter-text { font-size: 14px; line-height: 22px; color: var(--muted); width: 230px; }
  .signup { display: flex; margin-top: 18px; }
  .signup-input { width: 146px; height: 31px; background: var(--white); color: #555; font-size: 15px; padding-left: 24px; display: flex; align-items: center; border-radius: 3px 0 0 3px; }
  .signup-button { width: 66px; height: 31px; background: var(--orange); font-size: 16px; display: flex; align-items: center; justify-content: center; border-radius: 0 3px 3px 0; }
  .social { display: flex; gap: 8px; margin-top: 10px; }
  .social span { width: 25px; height: 25px; border: 1.5px solid var(--muted); border-radius: 50%; }
  .contact-list { list-style: none; font-size: 14px; line-height: 21px; color: var(--muted); }
  .contact-list li { display: flex; gap: 14px; align-items: flex-start; }
  .contact-list svg { flex: none; margin-top: 3px; }
</style>
</head>
<body>
<div class="page">
  <section class="hero" role="img" aria-label="Night skyline of high-rise towers beside a waterfront"></section>

  <nav class="main-nav">
    <a href="#" style="left:34px">HOME</a>
    <a href="#" style="left:138px">OUR TEAM</a>
    <a href="#" style="left:274px">OUR BLOG</a>
    <a href="#" style="left:706px">CONTACT US</a>
    <a href="#" class="client-login" style="left:873px">
      <svg width="22" height="18" viewBox="0 0 22 18" fill="none" stroke="#fff" stroke-width="1.6">
        <path d="M9 2a7 7 0 1 1 0 14"/><path d="M1 9h12M9 5l4 4-4 4"/>
      </svg>Clint Login</a>
  </nav>

  <div class="brand">
    <div class="brand-plate">
      <span class="brand-square"></span>
      <span class="brand-name">QUENBRICK<br>HALL</span>
    </div>
  </div>

  <h1 class="tagline">Your Paremier Partner</h1>
  <p class="tagline-sub">for all your development, real estate Property<br>management, and investing needs</p>

  <svg class="slider-arrow" style="left:0" width="80" height="124" viewBox="0 0 80 124" fill="none" stroke="#fff" stroke-width="2"><path d="M78 2 2 62l76 60"/></svg>
  <svg class="slider-arrow" style="left:1102px" width="80" height="124" viewBox="0 0 80 124" fill="none" stroke="#fff" stroke-width="2"><path d="M2 2l76 60-76 60"/></svg>

  <div class="services">
    <div class="service-tab">Develompment</div>
    <div class="service-tab is-active">Real Estate</div>
    <div class="service-tab">Property Management</div>
    <div class="service-tab">Construction</div>
    <div class="service-photo photo-development" role="img" aria-label="City highway at night with light trails"></div>
    <div class="service-photo photo-realestate" role="img" aria-label="Modern luxury house lit at dusk"></div>
    <div class="service-photo photo-property" role="img" aria-label="Bright furnished apartment interior"></div>
    <div class="service-photo photo-construction" role="img" aria-label="High-rise towers under construction"></div>
  </div>

  <div class="footer-col" style="left:85px">
    <h3 class="footer-title">Site Links</h3>
    <ul class="footer-list"><li>Home</li><li>Our Team</li><li>Our Blog</li><li>Contact Us</li></ul>
  </div>
  <div class="footer-col" style="left:319px; top:908px">
    <h3 class="footer-title">Services</h3>
    <ul class="footer-list"><li>Development</li><li>Real Estate</li><li>Property Management</li><li>Construction</li></ul>
  </div>
  <div class="footer-col" style="left:571px">
    <h3 class="footer-title">Stay in Touch</h3>
    <p class="newsletter-text">Subscribe our newsletter to stay up to date about new funds</p>
    <div class="signup"><span class="signup-input">email</span><span class="signup-button">Submit</span></div>
    <div class="social"><span></span><span></span><span></span></div>
  </div>
  <div class="footer-col" style="left:899px; top:906px">
    <h3 class="footer-title">Contact Us</h3>
    <ul class="contact-list">
      <li><svg width="14" height="18" viewBox="0 0 14 18" fill="#fff"><path d="M7 0a7 7 0 0 1 7 7c0 5-7 11-7 11S0 12 0 7a7 7 0 0 1 7-7zm0 4a3 3 0 1 0 0 6 3 3 0 0 0 0-6z"/></svg><span>4410 Ridgeline Avenue<br>Near Harbor</span></li>
      <li><svg width="14" height="16" viewBox="0 0 16 16" fill="none" stroke="#fff" stroke-width="1.6"><path d="M3 1l3 3-2 2a9 9 0 0 0 6 6l2-2 3 3-2 2C7 15 1 9 1 3z"/></svg><span>5550142876</span></li>
      <li><svg width="16" height="12" viewBox="0 0 16 12" fill="none" stroke="#fff" stroke-width="1.4"><rect x="1" y="1" width="14" height="10"/><path d="M1 1l7 6 7-6"/></svg><span>mail@quenbrickhall.com</span></li>
    </ul>
  </div>
</div>
</body>
</html>
```